Want to incorporate elements of all these items to make an amazing sign to welcome people to the community. The sign is 6x4 and needs to incorporate the following items:

Welcome to Corwick Meadows

Come visit the PRD sales center at 745 thistledown road
High Speed Fiber Internet
Land financing starting at $299 (No credit checks)
Let us build your dream home!
555-284-7390
We like the gold and black design no teal or blue that was another agents design. Some combination of the current sign all the stuff listed above and then design elements that tie into the truck wrap.

Target Market(s)

People visiting the neighborhood

Industry/Entity Type

real estate and construction

Font styles to use
Serif

Colors

Designer to choose colors to be used in the design.

Requirements
Must have
• PRD Home Builders Welcomes you to Corwick Meadows, Let us build your dream home, Phone number, Land financing starting at $299 NO credit checks

```html
<!DOCTYPE html>
<html lang="en">
<head>
<meta charset="utf-8">
<title>Welcome to Corwick Meadows – Community Sign</title>
<link rel="stylesheet" href="https://fonts.googleapis.com/css2?family=Playfair+Display:wght@900&family=Poppins:wght@500;600;700;800&display=swap">
<style>
  :root {
    --backdrop: #565658;
    --ink: #050505;
    --signal-red: #d6202f;
    --paper: #ffffff;
    --gold: #c99a32;
    --gold-light: #f4e07f;
    --silver-top: #e0dfdf;
    --silver-mid: #f4f4f6;
    --silver-low: #c8c6c7;
  }
  html, body {
    margin: 0;
    padding: 0;
    width: 1200px;
    height: 1047px;
    overflow: hidden;
    background: var(--backdrop);
  }
  .canvas { display: block; width: 1200px; height: 1047px; }
  .headline { font-family: "Playfair Display", Georgia, serif; font-weight: 900; fill: var(--ink); }
  .community-name { font-family: "Poppins", Arial, sans-serif; font-weight: 800; fill: var(--signal-red); }
  .feature { font-family: "Poppins", Arial, sans-serif; font-weight: 600; fill: var(--ink); }
  .visit-line { font-family: "Poppins", Arial, sans-serif; font-weight: 600; fill: var(--paper); }
  .phone-number { font-family: "Poppins", Arial, sans-serif; font-weight: 700; fill: var(--paper); }
  .tagline { font-family: "Poppins", Arial, sans-serif; font-weight: 500; fill: var(--paper); }
  .builder-name { font-family: "Poppins", Arial, sans-serif; font-weight: 700; fill: var(--ink); }
  .offer { font-family: "Poppins", Arial, sans-serif; font-weight: 500; fill: var(--ink); }
  .offer-note { font-family: "Poppins", Arial, sans-serif; font-weight: 500; fill: var(--signal-red); }
</style>
</head>
<body>
<svg class="canvas" viewBox="0 0 1200 1047" xmlns="http://www.w3.org/2000/svg">
  <defs>
    <linearGradient id="silver-panel" x1="0" y1="0" x2="0" y2="1">
      <stop offset="0" stop-color="var(--silver-top)"/>
      <stop offset="0.48" stop-color="var(--silver-mid)"/>
      <stop offset="1" stop-color="var(--silver-low)"/>
    </linearGradient>
    <linearGradient id="gold-bar" x1="0" y1="0" x2="1" y2="0">
      <stop offset="0" stop-color="#d9b64a"/>
      <stop offset="0.5" stop-color="var(--gold-light)"/>
      <stop offset="1" stop-color="#d9b64a"/>
    </linearGradient>
  </defs>

  <g class="sign">
    <rect class="sign__top-panel" x="142" y="211" width="916" height="311" fill="url(#silver-panel)"/>
    <rect class="sign__black-band" x="142" y="522" width="916" height="107" fill="var(--ink)"/>
    <rect class="sign__red-band" x="142" y="629" width="916" height="94" fill="var(--signal-red)"/>
    <rect class="sign__black-base" x="142" y="723" width="916" height="101" fill="var(--ink)"/>

    <text class="headline" x="173" y="352" font-size="158" textLength="857" lengthAdjust="spacingAndGlyphs">WELCOME</text>
    <text class="community-name" x="173" y="434" font-size="80" textLength="858" lengthAdjust="spacingAndGlyphs">TO CORWICK MEADOWS</text>
    <text class="feature" x="1033" y="491" font-size="39" text-anchor="end" textLength="504" lengthAdjust="spacingAndGlyphs">HIGH SPEED FIBER INTERNET</text>

    <text class="visit-line" x="1036" y="567" font-size="36" text-anchor="end" textLength="455" lengthAdjust="spacingAndGlyphs">COME VISIT THE PRD SALES</text>
    <text class="visit-line" x="1036" y="609" font-size="36" text-anchor="end" textLength="507" lengthAdjust="spacingAndGlyphs">CENTER AT 745 THISTLEDOWN RD</text>

    <g class="phone-icon" transform="translate(536 660)">
      <path d="M3 2 L11 0 L15 10 L10 14 C12 20 16 25 22 28 L26 23 L35 27 L34 35 L26 35 C12 33 2 22 0 9 Z" fill="var(--paper)"/>
    </g>
    <text class="phone-number" x="1035" y="701" font-size="70" text-anchor="end" textLength="446" lengthAdjust="spacingAndGlyphs">555-284-7390</text>

    <text class="tagline" x="1032" y="784" font-size="34" text-anchor="end" textLength="500" lengthAdjust="spacingAndGlyphs">Let us build your dream home!</text>

    <g class="offer-panel">
      <rect class="offer-panel__box" x="192" y="540" width="296" height="241" fill="var(--paper)" stroke="var(--gold)" stroke-width="12"/>
      <text class="builder-name" x="340" y="630" font-size="78" text-anchor="middle">PRD</text>
      <rect class="offer-bar" x="222" y="657" width="236" height="66" fill="url(#gold-bar)"/>
      <text class="offer" x="340" y="685" font-size="25" text-anchor="middle">Land financing</text>
      <text class="offer" x="340" y="715" font-size="25" text-anchor="middle">starting at $299</text>
      <text class="offer-note" x="340" y="752" font-size="24" text-anchor="middle">(No credit checks)</text>
    </g>
  </g>
</svg>
</body>
</html>
```